Stationery Design Project

I have recently had developed a logo for my new company Northwind Venture Partners -see logo attached.
I now need the following
1. Letterhead design as Word template
text needs to show the logo and then
Northwind Venture Partners Pty Ltd
ABN 83 402 615 294
Level 5, Harrow Building
17 Wexley Court
Baulkham Hills, NSW 2153
Tel: + 61(0)2 7314 2086
www.northwindventurepartners.example
dericp@northwindventurepartners.example
2. Business card -print ready -
Front side needs to show logo then text as follows
Deric Pellham
CEO
Level 5, Harrow Building
17 Wexley Court
Baulkham Hills, NSW 2153
T: + 61 (0)2 7314 2086
M: + 61 (0)438 772 104
dericp@brolvenco.example
On the back of the business card should appear the logo then text as follows
Correct text for the back of the card now in the attached word file please use bold and italics as indicated. Thanks
3. With compliments slip: Including logo + the web address www.northwindventurepartners.example
With compliments slip should fit 3 to an A4 sheet
4. Envelop design including logo + address
For the ethos of the company original brief for the logo below:
I am creating a new business advisory company called Northwind Venture Partners. the Web address will be www.northwindventurepartners.example This business is focused on assisting medium size businesses to achieve their growth objectives. The three pillars are self explanatory -it is focused on businesses that seek to build a global footprint, they seek to define/refine their business model and strategy, they are forward looking and focused on achieving growth.
The ethos of this company will be innovative thinking, passionate, dynamic, entrepreneurial this should reflected in the logo. That said the Logo should not be 'complicated' it should be simple and elegant...
Thanks Deric Pellham
Reason: I have been travelling all this week -so will only get a chance to review this weekend. Thanks
Target Market(s)
Medium sized business owners with sales between US$5m and $50m.
Industry/Entity Type
Business
Look and feel

```html
<!DOCTYPE html>
<html lang="en">
<head>
<meta charset="utf-8">
<title>Northwind Venture Partners – Stationery</title>
<link href="https://fonts.googleapis.com/css2?family=Lato:ital,wght@0,400;0,700;1,700&display=swap" rel="stylesheet">
<style>
:root{
  --bg:#e6e6e6;
  --paper:#ffffff;
  --ink:#3d3d3d;
  --ink-soft:#6a6a6a;
  --navy:#1d3f73;
  --blue:#1e73b8;
  --blue-dark:#0f4f8c;
  --blue-light:#3e9ad8;
  --window:#efefef;
}
*{box-sizing:border-box;margin:0;padding:0}
html,body{width:1200px;height:808px;overflow:hidden}
body{background:var(--bg);font-family:"Lato",sans-serif;color:var(--ink);position:relative}
.sheet{position:absolute;background:var(--paper);box-shadow:0 2px 6px rgba(0,0,0,.18)}
.brand{position:absolute;display:flex;align-items:flex-start;gap:7px}
.brand-mark{background:var(--blue);flex:none}
.brand-name{color:var(--ink);font-weight:700;line-height:1.08}
.icon{display:inline-block;flex:none}

/* letterhead */
.letterhead{left:48px;top:77px;width:517px;height:665px}
.letterhead .brand{left:40px;top:48px}
.letterhead .brand-mark{width:14px;height:14px;margin-top:3px}
.letterhead .brand-name{font-size:13px}
.lh-details{position:absolute;left:355px;top:45px;font-size:5.6px;line-height:1.6;color:var(--ink-soft)}
.lh-details .company{font-size:7.6px;font-weight:700;color:var(--ink);margin-bottom:2px}
.lh-details .addr{font-weight:700;color:var(--ink);margin:2px 0}
.lh-row{display:flex;align-items:center;gap:3px}
.lh-row .icon{width:6px;height:6px}
.lh-web{position:absolute;right:50px;bottom:27px;font-size:5.6px;font-weight:700;color:var(--ink)}

/* business card front */
.card-front{left:590px;top:85px;width:210px;height:119px}
.card-front .brand{left:24px;top:44px}
.card-front .brand-mark{width:8px;height:8px;margin-top:2px}
.card-front .brand-name{font-size:8px}
.cf-details{position:absolute;left:109px;top:20px;font-size:4.3px;line-height:1.5;color:var(--ink-soft)}
.cf-name{font-size:7px;font-weight:700;color:var(--navy);line-height:1.2}
.cf-role{margin-bottom:4px}
.cf-row{display:flex;align-items:center;gap:3px}
.cf-row .icon{width:5px;height:5px}
.gap{height:4px}

/* business card back */
.card-back{left:817px;top:85px;width:209px;height:119px;
  background:linear-gradient(120deg,var(--blue-dark) 0%,var(--blue) 55%,var(--blue-light) 100%);color:#fff;overflow:hidden}
.cb-decor{position:absolute;right:0;top:0;width:58px;height:119px;
  background:linear-gradient(180deg,rgba(255,255,255,.35),rgba(255,255,255,.08))}
.cb-title{position:absolute;left:12px;top:16px;font-size:8.4px;line-height:1.2}
.cb-title em{font-weight:700}
.cb-list{position:absolute;left:12px;top:41px;width:140px;list-style:none;font-size:4.3px;line-height:1.95;white-space:nowrap}
.cb-list li::before{content:"";display:inline-block;width:2.5px;height:2.5px;border-radius:50%;background:#fff;margin-right:3px;vertical-align:middle}
.cb-web{position:absolute;left:12px;bottom:14px;font-size:5.2px;font-weight:700}

/* envelope */
.envelope{left:590px;top:225px;width:569px;height:245px}
.envelope .brand,.slip .brand{left:52px;top:38px}
.envelope .brand-mark,.slip .brand-mark{width:12px;height:12px;margin-top:2px}
.envelope .brand-name,.slip .brand-name{font-size:12.5px}
.env-window{position:absolute;left:50px;top:120px;width:240px;height:74px;border-radius:12px;
  background:var(--window);box-shadow:inset 0 0 6px rgba(0,0,0,.12)}
.env-address{position:absolute;left:53px;top:217px;font-size:6px;font-weight:700;color:var(--ink-soft)}
.env-web{position:absolute;right:24px;top:217px;font-size:6px;font-weight:700;color:var(--ink)}

/* compliments slip */
.slip{left:605px;top:508px;width:540px;height:215px}
.slip-details{position:absolute;left:38px;top:165px;font-size:5.8px;line-height:1.65;color:var(--ink-soft)}
.slip-details .addr{font-weight:700;color:var(--ink)}
.slip-row{display:flex;align-items:center;gap:3px}
.slip-row .icon{width:7px;height:7px}
.slip-title{position:absolute;right:30px;top:166px;font-size:20px;color:var(--ink-soft);letter-spacing:-.2px}
.slip-title b{color:var(--ink)}
</style>
</head>
<body>

<section class="sheet letterhead" aria-label="Letterhead">
  <div class="brand"><span class="brand-mark"></span><span class="brand-name">Northwind<br>Venture<br>Partners</span></div>
  <div class="lh-details">
    <p class="company">Northwind Venture Partners Pty Ltd</p>
    <p>ABN 83 402 615 294</p>
    <p class="addr">Level 5, Harrow Building 17 Wexley Court<br>Merrin Vale ACT 2611</p>
    <p class="lh-row"><svg class="icon" viewBox="0 0 10 10"><circle cx="5" cy="5" r="4.5" fill="var(--navy)"/></svg>+ 61(0)2 7314 2086</p>
    <p class="lh-row"><svg class="icon" viewBox="0 0 10 10"><rect x="0.5" y="2" width="9" height="6" fill="var(--navy)"/></svg>dericp@northwindventurepartners.example</p>
  </div>
  <p class="lh-web">www.northwindventurepartners.example</p>
</section>

<section class="sheet card-front" aria-label="Business card front">
  <div class="brand"><span class="brand-mark"></span><span class="brand-name">Northwind<br>Venture<br>Partners</span></div>
  <div class="cf-details">
    <p class="cf-name">Deric Pellham</p>
    <p class="cf-role">CEO</p>
    <p>Level 5, Harrow Building<br>17 Wexley Court<br>Merrin Vale ACT 2611</p>
    <div class="gap"></div>
    <p class="cf-row"><svg class="icon" viewBox="0 0 10 10"><circle cx="5" cy="5" r="4.5" fill="var(--navy)"/></svg>www.northwindventurepartners.example</p>
    <div class="gap"></div>
    <p class="cf-row"><svg class="icon" viewBox="0 0 10 10"><circle cx="5" cy="5" r="4.5" fill="var(--navy)"/></svg>T: + 61 (0)2 7314 2086</p>
    <p class="cf-row"><svg class="icon" viewBox="0 0 10 10"><circle cx="5" cy="5" r="4.5" fill="var(--navy)"/></svg>M: + 61 (0)438 772 104</p>
    <div class="gap"></div>
    <p class="cf-row"><svg class="icon" viewBox="0 0 10 10"><circle cx="5" cy="5" r="4.5" fill="var(--navy)"/></svg>dericp@brolvenco.example</p>
  </div>
</section>

<section class="sheet card-back" aria-label="Business card back">
  <div class="cb-decor" role="img" aria-label="Large brand decoration area"></div>
  <p class="cb-title">Develop the <em>Right Strategy</em><br>for your business</p>
  <ul class="cb-list">
    <li>Create your <b>Advisory Board</b> and gain perspective</li>
    <li>Build the <b>Business Plan</b> your team will implement</li>
    <li>Take your business global - <b><i>Export Market Development</i></b></li>
    <li>Learn from your peers join our <b>CEO Groups</b></li>
    <li>Attend our <b>Presentations, Seminars and Conferences</b></li>
  </ul>
  <p class="cb-web">www.northwindventurepartners.example</p>
</section>

<section class="sheet envelope" aria-label="Envelope">
  <div class="brand"><span class="brand-mark"></span><span class="brand-name">Northwind<br>Venture<br>Partners</span></div>
  <div class="env-window"></div>
  <p class="env-address">Level 5, Harrow Building 17 Wexley Court Merrin Vale ACT 2611</p>
  <p class="env-web">www.northwindventurepartners.example</p>
</section>

<section class="sheet slip" aria-label="With compliments slip">
  <div class="brand"><span class="brand-mark"></span><span class="brand-name">Northwind<br>Venture<br>Partners</span></div>
  <div class="slip-details">
    <p class="addr">Level 5, Harrow Building 17 Wexley Court Merrin Vale ACT 2611</p>
    <p class="slip-row"><svg class="icon" viewBox="0 0 10 10"><circle cx="5" cy="5" r="4.5" fill="var(--navy)"/></svg>+ 61 (0)2 7314 2086
      <svg class="icon" viewBox="0 0 10 10"><circle cx="5" cy="5" r="4.5" fill="var(--navy)"/></svg>info@northwindventurepartners.example</p>
    <p>www.northwindventurepartners.example</p>
  </div>
  <p class="slip-title">with<b>Compliments</b></p>
</section>

</body>
</html>
```